Packaging for Devotional Books

I need a packaging design for Devotional Christian books which I will package and sell to the public. Design should be unique, interesting and something beautiful that they would want to treasure or want. It should come across all genders and age groups. (girl, boys, teens, moms, dads). This packaging would serve as a gift. Box size is around 9x6x11.5". My goal is to create a beautiful gift, with the feeling of excitement, without the feel of having to give "boring" devotional books. Must include this message:
"This gift is a treasure in your heart forever.
Picked by someone special for you.
Love shared, wisdom to be imparted;
Read it and it becomes you.
Once blessed, soon it will be your turn,
To give out something that the world needs to go on."

Target Market(s)

All ages

Industry/Entity Type

Christian

Font styles to use
Decorative

Requirements
Must have
• Never boring
Nice to have
• Must come across all ages and genders
Should not have
• Please do not use script as font.

```html
<!DOCTYPE html>
<html lang="en">
<head>
<meta charset="utf-8">
<title>Devotional Gift Box Lids</title>
<link rel="stylesheet" href="https://fonts.googleapis.com/css2?family=Amatic+SC:wght@400;700&display=swap">
<style>
  :root {
    --page: #efece7;
    --lid-white: #ffffff;
    --lid-grey: #ececec;
    --ink: #2b2b33;
    --ink-soft: #55555e;
    --line-black: #3a3a3a;
    --swirl-purple: #5b3fa3;
    --silver-edge: #b9b9b9;
    --silver-mid: #e6e6e6;
  }
  * { box-sizing: border-box; margin: 0; padding: 0; }
  html, body { width: 1200px; height: 849px; overflow: hidden; }
  body {
    background: var(--page);
    font-family: "Amatic SC", "Trebuchet MS", sans-serif;
    color: var(--ink);
  }
  .lid-grid {
    position: absolute; left: 40px; top: 44px;
    display: grid;
    grid-template-columns: repeat(3, 340px);
    grid-template-rows: repeat(2, 360px);
    gap: 40px 50px;
  }
  .lid {
    position: relative; overflow: hidden;
    background: var(--lid-white);
    box-shadow: 0 2px 10px rgba(0,0,0,.12);
    display: flex; flex-direction: column; align-items: center;
  }
  .message {
    position: relative;
    text-align: center;
    font-size: 15px; line-height: 1.3; letter-spacing: 1.1px;
    color: var(--ink-soft);
  }
  .message .spaced { margin-top: 6px; }

  /* Lid 1: botanical line art */
  .lid--botanical { justify-content: center; gap: 8px; padding: 18px 0; }
  .lid--botanical .art {
    width: 220px; height: 84px; flex: none;
    background: radial-gradient(ellipse at center, #cfcfcf 0%, #f2f2f2 70%, #fff 100%);
  }
  .lid--botanical .rule { width: 230px; height: 1px; background: var(--line-black); flex: none; }

  /* Lids 2 & 4: paisley */
  .lid--paisley { background: var(--lid-grey); }
  .lid--paisley .art { width: 100%; height: 170px; }
  .lid--paisley.grey .art { background: linear-gradient(180deg, #a9a49c 0%, #c9c5bf 60%, var(--lid-grey) 100%); }
  .lid--paisley.blue .art { background: linear-gradient(180deg, #6d98c4 0%, #a9c3de 60%, var(--lid-grey) 100%); }
  .lid--paisley .message { margin-top: 24px; }

  /* Lid 3: silver with purple swirl */
  .lid--silver {
    background: radial-gradient(ellipse at 50% 45%, var(--silver-mid) 0%, #d3d3d3 60%, var(--silver-edge) 100%);
  }
  .lid--silver .pattern { position: absolute; inset: 0 0 auto 0; height: 120px;
    background: linear-gradient(180deg, rgba(255,255,255,.35), rgba(255,255,255,0)); }
  .lid--silver .swirl {
    margin-top: 100px; width: 300px; height: 60px;
    background: linear-gradient(90deg, rgba(91,63,163,.15), var(--swirl-purple) 35%, #8a74c8 65%, rgba(91,63,163,.15));
    border-radius: 30px;
  }
  .lid--silver .message { margin-top: 20px; }

  /* Lid 5: rings */
  .lid--rings { flex-direction: row; align-items: flex-start; }
  .lid--rings .art {
    width: 150px; height: 300px; margin: 30px 0 0 10px; flex: none;
    background: linear-gradient(160deg, #e8f4fb 0%, #d8d8d8 45%, #e4f3ec 80%, #f5f5f5 100%);
  }
  .lid--rings .message {
    text-align: right; margin: 24px 18px 0 auto;
    font-size: 14px; line-height: 1.2;
  }
  .lid--rings .message .big { font-size: 18px; letter-spacing: 2px; }

  /* Lid 6: stars */
  .lid--stars { justify-content: center; }
  .lid--stars .message { font-size: 18px; line-height: 1.35; color: var(--ink); }
  .lid--stars .stars { position: absolute; inset: 0; }
</style>
</head>
<body>
<main class="lid-grid">

  <section class="lid lid--botanical">
    <div class="art" role="img" aria-label="Black line-art wildflower bouquet"></div>
    <div class="rule"></div>
    <div class="message">
      <p>This gift is a treasure</p>
      <p>in your heart forever.</p>
      <p>Picked by someone special for you.</p>
      <p>Love shared, wisdom to be imparted;</p>
      <p>Read it and it becomes you.</p>
      <p>Once blessed, soon it will be your turn,</p>
      <p class="spaced">To give out something that the world needs to go on.</p>
    </div>
    <div class="rule"></div>
    <div class="art" role="img" aria-label="Black line-art wildflowers mirrored below the message"></div>
  </section>

  <section class="lid lid--paisley grey">
    <div class="art" role="img" aria-label="Grey hand-drawn paisley and flower pattern"></div>
    <div class="message">
      <p>This gift is a treasure</p>
      <p>in your heart forever.</p>
      <p>Picked by someone special for you.</p>
      <p>Love shared, wisdom to be imparted;</p>
      <p>Read it and it becomes you.</p>
      <p>Once blessed, soon it will be your turn,</p>
      <p>To give out something that the world needs to go on.</p>
    </div>
  </section>

  <section class="lid lid--silver">
    <div class="pattern" role="img" aria-label="Faint white floral swirls on silver"></div>
    <div class="swirl" role="img" aria-label="Purple flowing floral swirl band"></div>
    <div class="message">
      <p>This gift is a treasure</p>
      <p>in your heart forever.</p>
      <p>Picked by someone special for you.</p>
      <p>Love shared, wisdom to be imparted;</p>
      <p>Read it and it becomes you.</p>
      <p>Once blessed, soon it will be your turn,</p>
      <p>To give out something that the world needs to go on.</p>
    </div>
  </section>

  <section class="lid lid--paisley blue">
    <div class="art" role="img" aria-label="Blue hand-drawn paisley and flower pattern"></div>
    <div class="message">
      <p>This gift is a treasure</p>
      <p>in your heart forever.</p>
      <p>Picked by someone special for you.</p>
      <p>Love shared, wisdom to be imparted;</p>
      <p>Read it and it becomes you.</p>
      <p>Once blessed, soon it will be your turn,</p>
      <p>To give out something that the world needs to go on.</p>
    </div>
  </section>

  <section class="lid lid--rings">
    <div class="art" role="img" aria-label="Sketchy black rings with blue, red and green accents"></div>
    <div class="message">
      <p class="big">This gift is a treasure</p>
      <p>in your heart forever.</p>
      <p class="big">Picked by someone</p>
      <p class="big">special for you.</p>
      <p>Love shared,</p>
      <p>wisdom to be imparted;</p>
      <p class="big">Read it and</p>
      <p>it becomes you.</p>
      <p>Once blessed,</p>
      <p>soon it will be</p>
      <p class="big">your turn,</p>
      <p>to give out</p>
      <p>something that</p>
      <p>the world needs</p>
      <p class="big">to go on.</p>
    </div>
  </section>

  <section class="lid lid--stars">
    <svg class="stars" width="340" height="360" viewBox="0 0 340 360" aria-hidden="true">
      <g fill="none" stroke="#222" stroke-width="1.6" stroke-linejoin="round">
        <polygon points="30,16 33,24 42,24 35,29 38,38 30,32 22,38 25,29 18,24 27,24"/>
        <polygon points="180,12 182,18 188,18 183,22 185,28 180,24 175,28 177,22 172,18 178,18"/>
        <polygon points="305,16 308,24 317,24 310,29 313,38 305,32 297,38 300,29 293,24 302,24"/>
        <polygon points="18,170 20,175 25,175 21,178 23,183 18,180 13,183 15,178 11,175 16,175"/>
        <polygon points="322,150 324,155 329,155 325,158 327,163 322,160 317,163 319,158 315,155 320,155"/>
        <polygon points="28,318 31,326 40,326 33,331 36,340 28,334 20,340 23,331 16,326 25,326"/>
        <polygon points="310,318 313,325 321,325 315,330 317,338 310,333 303,338 305,330 299,325 307,325"/>
        <polygon points="150,328 152,333 157,333 153,336 155,341 150,338 145,341 147,336 143,333 148,333"/>
      </g>
    </svg>
    <div class="message">
      <p>This gift is a treasure</p>
      <p>in your heart forever.</p>
      <p>Picked by someone special for you.</p>
      <p>Love shared,</p>
      <p>wisdom to be imparted;</p>
      <p>Read it and it becomes you.</p>
      <p>Once blessed,</p>
      <p>soon it will be your turn,</p>
      <p>To give out something that</p>
      <p>the world needs to go on.</p>
    </div>
  </section>

</main>
</body>
</html>
```